Geschäftspapiere für Lasergravuren
Zielgruppe
Lasergravuren z.B. auf Glas, Holz, Filz, Papier, Acryl, eloxierten Aluminium zu Dekorationszwecken,
Ausschneiden von Elementen z.B. aus Holz, Filz, Papier, Acryl usw. zu Dekorationszwecken mit dem Lasergravierer.
Anfertigung verschiedener Dekorationsartikel,
Zielgruppe: Frauen (mit Familien) aller Altersgruppen, die Freude am Dekorieren und Verschenken haben
Aufgabenstellung
Das vorhandene Logo soll mit eingebunden werden

```html
<!DOCTYPE html>
<html lang="de">
<head>
<meta charset="utf-8">
<title>Lumora – Briefbogen</title>
<link rel="stylesheet" href="https://fonts.googleapis.com/css2?family=Open+Sans:wght@400;600&family=Arimo:wght@400&display=swap">
<style>
  :root {
    --gold: #b08440;
    --gold-light: #c9a46e;
    --beige: #dcc4a2;
    --grey: #6e6e6e;
    --text: #5c5c5c;
    --paper: #ffffff;
  }
  * { margin: 0; padding: 0; box-sizing: border-box; }
  html, body { width: 866px; height: 1200px; overflow: hidden; background: var(--paper); }
  .letterhead {
    position: relative;
    width: 866px;
    height: 1200px;
    background: var(--paper);
    font-family: "Open Sans", Arial, sans-serif;
    color: var(--text);
  }
  .top-band { position: absolute; left: 0; top: 0; }
  .brand {
    position: absolute;
    left: 530px;
    top: 52px;
    width: 300px;
    display: flex;
    align-items: center;
    gap: 16px;
  }
  .brand-dot {
    width: 72px; height: 72px;
    border: 2px solid var(--gold);
    border-radius: 50%;
    flex: none;
  }
  .brand-name {
    font-size: 40px;
    font-weight: 400;
    color: var(--grey);
    letter-spacing: 1px;
    margin-left: 28px;
  }
  .divider {
    position: absolute;
    left: 612px;
    top: 42px;
    width: 1px;
    height: 206px;
    background: var(--gold);
  }
  .contact {
    position: absolute;
    left: 630px;
    top: 150px;
    font-size: 14.5px;
    line-height: 19px;
  }
  .address { margin-bottom: 12px; }
  .contact-list { list-style: none; }
  .contact-list li { display: flex; align-items: center; gap: 9px; }
  .contact-list svg { width: 11px; height: 11px; fill: var(--gold); flex: none; }
  .sender-line {
    position: absolute;
    left: 91px;
    top: 214px;
    font-family: "Arimo", Arial, sans-serif;
    font-size: 9.5px;
    color: var(--text);
    padding-bottom: 1px;
    border-bottom: 1px solid #9a9a9a;
  }
  .sender-line .sep { color: var(--gold); }
  .fold-mark {
    position: absolute;
    left: 0;
    width: 31px;
    height: 1px;
    background: var(--gold);
  }
  .fold-mark.upper { top: 421px; }
  .fold-mark.lower { top: 823px; }
  .bottom-band { position: absolute; left: 0; bottom: 0; }
</style>
</head>
<body>
<main class="letterhead">
  <svg class="top-band" width="520" height="22" viewBox="0 0 520 22" aria-hidden="true">
    <polygon points="0,0 512,0 494,20 0,20" fill="var(--grey)"/>
    <polygon points="72,0 106,0 88,20 54,20" fill="var(--paper)"/>
    <polygon points="80,0 98,0 80,20 62,20" fill="var(--beige)"/>
    <polygon points="106,0 124,0 106,20 88,20" fill="var(--gold-light)"/>
    <polygon points="132,0 150,0 132,20 114,20" fill="var(--gold)"/>
    <polygon points="150,0 176,0 158,20 132,20" fill="var(--paper)"/>
  </svg>

  <div class="brand">
    <span class="brand-dot"></span>
    <span class="brand-name">Lumora</span>
  </div>

  <div class="divider"></div>

  <address class="contact" style="font-style:normal">
    <div class="address">Lindenweg 12<br>31135 Musterstadt</div>
    <ul class="contact-list">
      <li><svg viewBox="0 0 12 12"><path d="M2 0.5l2.2 0.4 0.8 2.6-1.4 1.1c0.7 1.5 1.8 2.6 3.3 3.3l1.1-1.4 2.6 0.8 0.4 2.2c-0.4 1.1-1.4 1.8-2.5 1.5C4.600 10.2 1.800 7.400 0.5 3.5 0.200 2.400 0.900 1.000 2 0.5z"/></svg>0511 / 123 45 67</li>
      <li><svg viewBox="0 0 12 12"><path d="M3 0h6v3H3z M1 3.5h10v5H9.5V7h-7v1.5H1z M3 7.8h6V12H3z"/></svg>0511 / 123 45 68</li>
      <li><svg viewBox="0 0 12 12"><path d="M6 0a6 6 0 1 0 0.001 0zM6 1.2c0.7 0.6 1.2 1.9 1.3 3.3H4.7C4.800 3.100 5.300 1.800 6 1.2zM1.3 5.5h2.4c0.05 1.2 0.3 2.3 0.8 3.2A4.8 4.8 0 0 1 1.3 5.5zm0-1A4.8 4.8 0 0 1 4.5 2.3c-0.5 0.9-0.75 1.8-0.8 2.2zm3.4 1h2.6c-0.1 1.4-0.6 2.600-1.3 3.300-0.7-0.7-1.2-1.9-1.3-3.3zm3.600 0h2.400a4.8 4.8 0 0 1-3.200 3.200c0.500-0.900 0.750-2 0.800-3.200zm0-1c-0.05-0.4-0.3-1.3-0.8-2.2a4.8 4.8 0 0 1 3.200 2.200z"/></svg>www.lumora-deko.de</li>
      <li><svg viewBox="0 0 12 12"><path d="M0 4l6-3.5 6 3.5v7.5H0z M1.5 4.6 6 7.4l4.5-2.8L6 2.1z" fill-rule="evenodd"/></svg>post@lumora-deko.de</li>
    </ul>
  </address>

  <p class="sender-line">Gartenstraße 8 <span class="sep">|</span> 30159 Beispielstadt</p>

  <span class="fold-mark upper"></span>
  <span class="fold-mark lower"></span>

  <svg class="bottom-band" width="866" height="70" viewBox="0 0 866 70" aria-hidden="true">
    <circle cx="823" cy="18" r="9" fill="none" stroke="var(--gold)" stroke-width="2"/>
    <polygon points="0,36 866,36 866,52 0,52" fill="var(--gold)"/>
    <polygon points="0,55 866,55 866,59 0,59" fill="var(--grey)"/>
    <polygon points="0,62 866,62 866,66 0,66" fill="var(--gold)"/>
    <polygon points="790,34 866,34 866,50 824,62" fill="var(--paper)"/>
  </svg>
</main>
</body>
</html>
```